TRENDY & MODERN BUSINESS CARD DESIGN for Media Company *

I need a minimalistic - clean - modern and professional business card layout and design for MEDIA & PHOTOGRAPHY STUDIO.

We do NOT have a logo, and not really looking for one - but rather excellent typography and design. We would consider the 3 as a focal point.

We do personal and commercial photography.

Target Market(s)

Personal and commercial photography clientele

Contact Information for Business Card

ZUB size - from zub.com / size guidelines are enclosed in the brief

Font styles to use
Sans Serif

Colors
f78f20
eda3c7
cee9f5
0555a3
e667a6
fbf289

Requirements
Must have
• Clean lines - Modern layout
Nice to have
• All blue background as an option - use color palette in brief please.
Should not have
• Old fashion fonts and regular fonts.

```html
<!DOCTYPE html>
<html lang="en">
<head>
<meta charset="utf-8">
<title>Northlight Studio – Business Card</title>
<link href="https://fonts.googleapis.com/css2?family=Open+Sans:wght@400;600&family=Caveat:wght@500&display=swap" rel="stylesheet">
<style>
  :root {
    --backdrop: #6b6b6d;
    --card: #f7f8f8;
    --ink: #2f55a4;
    --swatch-yellow: #f3ea94;
    --swatch-pink: #d9a3c3;
    --swatch-sky: #cfe3ee;
    --shadow: rgba(0,0,0,0.28);
  }
  * { box-sizing: border-box; margin: 0; padding: 0; }
  html, body {
    width: 1200px; height: 971px; overflow: hidden;
    background: var(--backdrop);
    font-family: "Open Sans", Arial, sans-serif;
    color: var(--ink);
  }
  .sheet {
    width: 1200px; height: 971px;
    display: flex; align-items: center; justify-content: center; gap: 40px;
  }
  .card {
    position: relative;
    width: 540px; height: 309px;
    background: var(--card);
    box-shadow: 0 10px 24px var(--shadow);
    overflow: hidden;
  }

  /* Front */
  .card-front .wordmark {
    position: absolute; left: 0; right: 0; top: 100px;
    text-align: center;
  }
  .card-front .brand-name {
    display: inline-block;
    font-weight: 600; font-size: 34px; letter-spacing: 2px;
    padding: 0 12px 4px;
    border-bottom: 1.5px solid var(--ink);
  }
  .card-front .tagline {
    margin-top: 6px;
    font-size: 13px; letter-spacing: 0.5px;
  }
  .card-front .locations {
    position: absolute; left: 0; right: 0; bottom: 24px;
    text-align: center;
    font-size: 11px; letter-spacing: 2.4px;
  }

  /* Back */
  .card-back .person {
    position: absolute; right: 60px; top: 64px;
    text-align: right;
  }
  .card-back .person-name {
    font-family: "Caveat", cursive;
    font-weight: 500; font-size: 40px; line-height: 1;
  }
  .card-back .person-role {
    font-size: 9px; margin-top: 2px;
  }
  .contact-list {
    position: absolute; left: 54px; top: 136px;
    list-style: none;
  }
  .contact-item {
    display: flex; align-items: center;
  }
  .contact-item .swatch {
    width: 34px; display: flex; align-items: center; justify-content: center;
    flex-shrink: 0;
  }
  .contact-item.phone .swatch { background: var(--swatch-yellow); height: 42px; }
  .contact-item.email .swatch { background: var(--swatch-pink); height: 42px; }
  .contact-item.address .swatch { background: var(--swatch-sky); height: 66px; }
  .contact-item .detail {
    margin-left: 14px; font-size: 13px; line-height: 1.35;
  }
</style>
</head>
<body>
<main class="sheet">

  <section class="card card-front" aria-label="Business card front">
    <div class="wordmark">
      <div class="brand-name">NORTHLIGHT STUDIO</div>
      <p class="tagline">Framing Moments.&nbsp; Making Art.</p>
    </div>
    <p class="locations">Orlando &bull; Boston &bull; Denver &bull; Tulum</p>
  </section>

  <section class="card card-back" aria-label="Business card back">
    <div class="person">
      <div class="person-name">Marisol Vega</div>
      <div class="person-role">Founder &amp; Media Director</div>
    </div>

    <ul class="contact-list">
      <li class="contact-item phone">
        <span class="swatch">
          <svg width="16" height="16" viewBox="0 0 24 24" aria-hidden="true">
            <path fill="#2f55a4" d="M6.6 10.8a15.1 15.1 0 0 0 6.6 6.6l2.2-2.2a1 1 0 0 1 1-.25 11.4 11.4 0 0 0 3.6.57 1 1 0 0 1 1 1V20a1 1 0 0 1-1 1A17 17 0 0 1 3 4a1 1 0 0 1 1-1h3.5a1 1 0 0 1 1 1c0 1.250.2 2.45.57 3.57a1 1 0 0 1-.25 1z"/>
          </svg>
        </span>
        <span class="detail">(305) 555-0148</span>
      </li>
      <li class="contact-item email">
        <span class="swatch">
          <svg width="18" height="14" viewBox="0 0 18 14" aria-hidden="true">
            <rect x="0.5" y="0.5" width="17" height="13" fill="#2f55a4"/>
            <path d="M1 1l8 6.5L17 1M1 13l6-5.5M17 13l-6-5.5" stroke="#d9a3c3" stroke-width="1.2" fill="none"/>
          </svg>
        </span>
        <span class="detail">mv@northlightstudio.com</span>
      </li>
      <li class="contact-item address">
        <span class="swatch">
          <svg width="14" height="20" viewBox="0 0 14 20" aria-hidden="true">
            <path fill="#2f55a4" d="M7 0a7 7 0 0 0-7 7c0 5.2 7 13 7 13s7-7.8 7-13a7 7 0 0 0-7-7zm0 9.8A2.8 2.8 0 1 1 7 4.2a2.8 2.8 0 0 1 0 5.6z"/>
          </svg>
        </span>
        <span class="detail">2400 Coral Way<br>4th Floor<br>Miami, FL 33145</span>
      </li>
    </ul>
  </section>

</main>
</body>
</html>
```